LTV Business Card

This is a wide-range political consulting firm specializing in high-profile political campaigns. Red should be a predominant color in the business card, since this is a Heartland Party inspired consulting firm, but the word "heartland" will not appear anywhere in any kind of literature. Look has to be clean and crisp. The design should be forward thinking and appropriate for a company that is trying to break away from a traditionally "stodgy" image in politics.

Target Market(s)

potential national political candidates, wealthy donors,

Industry/Entity Type

Political

Contact Information for Business Card

Lionel T. Vardmoor
Political Consultant
438 Ormond Lane NW
#356
Washington, DC 20471

```html
<!DOCTYPE html>
<html lang="en">
<head>
<meta charset="utf-8">
<title>LTV Business Card</title>
<link rel="stylesheet" href="https://fonts.googleapis.com/css2?family=Mulish:wght@400;700;800&display=swap">
<style>
  :root {
    --backdrop: #4b4b4c;
    --paper: #f6f6f4;
    --ink: #2b2b2b;
    --ink-soft: #3a3a3a;
    --crimson: #8f121a;
    --crimson-deep: #7a0d13;
    --crimson-band: #9c2a30;
    --card-text-light: #f3e9e9;
  }
  html, body {
    margin: 0;
    padding: 0;
    width: 1200px;
    height: 1000px;
    overflow: hidden;
    background: var(--backdrop);
    font-family: "Mulish", "Century Gothic", sans-serif;
  }
  .canvas {
    position: relative;
    width: 1200px;
    height: 1000px;
  }
  .card {
    position: absolute;
    width: 530px;
    height: 302px;
    border-radius: 14px;
    overflow: hidden;
    box-shadow: 0 4px 10px rgba(0,0,0,0.35);
  }
  .card--front {
    left: 165px;
    top: 163px;
    background: var(--paper);
    color: var(--ink);
  }
  .card--back {
    left: 473px;
    top: 550px;
    background: linear-gradient(160deg, var(--crimson) 0%, var(--crimson-deep) 100%);
    color: var(--card-text-light);
  }
  .card__name {
    position: absolute;
    left: 39px;
    top: 40px;
    margin: 0;
    font-size: 20px;
    font-weight: 800;
    letter-spacing: 0.5px;
  }
  .card__title {
    position: absolute;
    left: 39px;
    top: 65px;
    margin: 0;
    font-size: 13px;
    font-weight: 400;
  }
  .card--front .card__title { color: var(--crimson); }
  .card__contact {
    position: absolute;
    left: 39px;
    top: 241px;
    margin: 0;
    font-size: 12.5px;
    line-height: 16px;
    font-style: normal;
  }
  .card--front .card__contact { color: var(--ink-soft); }
  .card__contact strong { font-weight: 700; }
  .card__band {
    position: absolute;
    left: 0;
    right: 0;
    bottom: 0;
    height: 20px;
  }
  .card--front .card__band { background: var(--crimson); }
  .card--back .card__band { background: var(--crimson-band); height: 22px; opacity: 0.85; }
</style>
</head>
<body>
<main class="canvas">
  <section class="card card--front" aria-label="Business card front">
    <h1 class="card__name">LIONEL T. VARDMOOR</h1>
    <p class="card__title">Political Consultant</p>
    <address class="card__contact">
      <strong>Tel:</strong> 202-555-0148 · <strong>Email:</strong> ltvardmoor@ltvstrategy.com<br>
      438 Ormond Lane NW #356, Washington, DC 20471
    </address>
    <div class="card__band"></div>
  </section>

  <section class="card card--back" aria-label="Business card reverse">
    <h2 class="card__name">LIONEL T. VARDMOOR</h2>
    <p class="card__title">Political Consultant</p>
    <address class="card__contact">
      <strong>Tel:</strong> 202-555-0148 · <strong>Email:</strong> ltvardmoor@ltvstrategy.com<br>
      438 Ormond Lane NW #356, Washington, DC 20471
    </address>
    <div class="card__band"></div>
  </section>
</main>
</body>
</html>
```